Zumbora Gutschein-Gewinnspiel
Aufgabenstellung
Design für ein Gewinnspiel bei dem es einen 1000 Euro Zumbora.de Gutschein zu gewinnen gibt.
Menüpunkte: Startseite, Teilnahmebedingungen, Preisdetails, Teilnehmen, Datenschutz.
Es soll eine Intro-Seite auf der der Preis groß heraus gestellt ist gestaltet werden mit den entsprechenden Menüpunkten sowie eine Template-Seite in der wir dann alle notwendigen Inhalte einfügen können. Von der Gestaltung her seid Ihr frei.
Gewinnspiel von uns finden Sie auf www.glueckspfad-beispiel.de damit Sie sich ein Bild über die bisherigen Gewinnspiele machen können.
WICHTIG: Es soll nur die Eingangsseite und eine Template Seite erstellt werden. Die komplette Programmierung bzw. Füllung mit Inhalten wird von uns gemacht! Für die Templateseite wäre eine Breite von 500 Pixeln oder mehr im Bereich wo wir Inhalte einfügen können wünschenswert.
„Normales altbackenes“ HTML mit Tabellen ohne großen CSS Schnick-Schnack würden wir bevorzugen da es für uns einfacher zum Bearbeiten ist.
Das Gewinnspiel wird später auf einer Subdomain laufen und hat somit keinen Domainnamen den man im Titel darstellen kann oder muss.
Das fertige Layout soll dann als geschnittene HTML Datei mit verlinkten Grafiken geliefert werden.
Grafik vom Gutschein ist hier zu finden:
https://bilder-eu.cdn-zumbora-beispiel.de/images/K/07/gs/motive/druck/gs_allgemein_04_de/gs_allgemein_04_de._X847201635_.gif

```html
<!DOCTYPE html>
<html lang="de">
<head>
<meta charset="utf-8">
<title>Zumbora Gutschein-Gewinnspiel</title>
<link rel="stylesheet" href="https://fonts.googleapis.com/css2?family=Didact+Gothic&family=Mulish:wght@600;700;800&display=swap">
<style>
  :root {
    --orange: #f2921d;
    --orange-light: #eca64b;
    --blue: #1f63a8;
    --blue-dark: #1d5f9f;
    --blue-text: #2a66a8;
    --footer-top: #2569ad;
    --footer-bottom: #5a9ad6;
    --footer-link: #123f73;
    --nav-bg: #e6e6e8;
    --grey-bar: #e2e2e2;
    --title-brown: #7e5340;
    --white: #ffffff;
  }
  * { margin: 0; padding: 0; box-sizing: border-box; }
  html, body { width: 1200px; height: 1134px; overflow: hidden; background: var(--white); }
  body { position: relative; font-family: "Didact Gothic", "Century Gothic", sans-serif; color: var(--blue-text); }

  .brand-bar {
    position: absolute; left: 0; top: 51px; width: 409px; height: 64px;
    background: var(--grey-bar); border-radius: 0 32px 32px 0;
    box-shadow: 2px 4px 6px rgba(0,0,0,.25);
  }
  .brand-pill {
    position: absolute; left: 222px; top: 58px; width: 175px; height: 50px;
    background: var(--white); border-radius: 25px;
    display: flex; align-items: center; justify-content: center;
    font-family: "Mulish", sans-serif; font-weight: 700; font-size: 24px; color: #222;
  }

  .title-art { position: absolute; left: 0; top: 0; width: 1200px; height: 300px; z-index: 3; pointer-events: none; }

  .promo-band {
    position: absolute; left: 0; top: 352px; width: 1200px; height: 74px;
    background: var(--orange-light);
  }

  .stage {
    position: absolute; left: 165px; top: 182px; width: 877px; height: 780px;
    background: var(--orange); border-radius: 130px 130px 110px 110px;
    box-shadow: 0 6px 10px rgba(0,0,0,.25);
  }

  .main-nav {
    position: absolute; left: 172px; top: 292px; width: 861px; height: 34px; z-index: 4;
    background: var(--nav-bg); border-radius: 17px;
    display: flex; align-items: center; justify-content: space-between; padding: 0 11px 0 12px;
    box-shadow: inset 0 1px 2px rgba(0,0,0,.2);
  }
  .main-nav a { color: var(--blue-text); text-decoration: none; font-size: 23px; line-height: 30px; padding: 0 8px; }
  .main-nav a.is-active { background: var(--blue-dark); color: var(--orange); border-radius: 15px; }

  .prize-strip {
    position: absolute; left: 165px; top: 356px; width: 877px; height: 70px; z-index: 2;
    background: linear-gradient(#f6b873, #eea24e);
    display: flex; align-items: center; justify-content: center;
  }
  .prize-headline {
    font-family: "Mulish", sans-serif; font-weight: 800; font-size: 40px; letter-spacing: 1px;
    color: var(--blue); text-shadow: 0 0 4px #fff, 0 0 8px #fff, 0 0 2px #fff;
  }

  .content {
    position: absolute; left: 182px; top: 428px; width: 841px; height: 516px; z-index: 2;
    background: var(--white); border-radius: 0 0 88px 88px;
    box-shadow: 0 3px 6px rgba(0,0,0,.2);
  }
  .content h2 {
    position: absolute; font-family: "Mulish", sans-serif; font-weight: 700; font-size: 21px; color: var(--blue-dark);
  }
  .content p {
    position: absolute; text-align: justify; color: var(--blue-text); hyphens: auto;
  }
  .intro-title { left: 48px; top: 31px; }
  .intro-text { left: 48px; top: 72px; width: 735px; font-size: 16.3px; line-height: 14.8px; }
  .col-left-title { left: 48px; top: 279px; }
  .col-left-text { left: 48px; top: 322px; width: 349px; font-size: 17.5px; line-height: 14.9px; }
  .col-right-title { left: 435px; top: 279px; }
  .col-right-text { left: 435px; top: 322px; width: 349px; font-size: 17.5px; line-height: 14.9px; }

  .site-footer {
    position: absolute; left: 0; top: 1054px; width: 1200px; height: 80px;
    background: linear-gradient(var(--footer-top), var(--footer-bottom));
    box-shadow: 0 -4px 8px rgba(0,0,0,.2);
    display: flex; align-items: center; justify-content: center; gap: 26px;
  }
  .site-footer a { color: var(--footer-link); text-decoration: none; font-size: 23px; }
</style>
</head>
<body>
  <div class="brand-bar"></div>
  <div class="brand-pill">Zumbora.de</div>

  <div class="promo-band"></div>
  <div class="stage"></div>

  <svg class="title-art" viewBox="0 0 1200 300" aria-hidden="true">
    <defs>
      <linearGradient id="titleBlue" x1="0" y1="0" x2="0" y2="1">
        <stop offset="0" stop-color="#7fa6dc"/>
        <stop offset="0.5" stop-color="#3f74bd"/>
        <stop offset="1" stop-color="#2a5ea8"/>
      </linearGradient>
      <filter id="titleGlow" x="-10%" y="-10%" width="120%" height="120%">
        <feGaussianBlur stdDeviation="3" in="SourceAlpha" result="b"/>
        <feFlood flood-color="#fff" flood-opacity=".9"/>
        <feComposite in2="b" operator="in" result="g"/>
        <feMerge><feMergeNode in="g"/><feMergeNode in="SourceGraphic"/></feMerge>
      </filter>
    </defs>
    <text x="282" y="250" textLength="605" lengthAdjust="spacingAndGlyphs"
          font-family="Mulish, sans-serif" font-weight="800" font-size="100"
          fill="var(--title-brown)" fill-opacity=".85">Gewinnspiel</text>
    <text x="282" y="250" textLength="620" lengthAdjust="spacingAndGlyphs"
          font-family="Mulish, sans-serif" font-weight="800" font-size="90"
          fill="url(#titleBlue)" filter="url(#titleGlow)"
          transform="rotate(-16 282 250)">Gewinnspiel</text>
  </svg>

  <nav class="main-nav">
    <a href="#">Startseite</a>
    <a href="#" class="is-active">Teilnahmebedingungen</a>
    <a href="#">Preisdetails</a>
    <a href="#">Teilnehmen</a>
    <a href="#">Datenschutz</a>
  </nav>

  <div class="prize-strip">
    <h1 class="prize-headline">1.000 € Geschenkgutschein gewinnen !</h1>
  </div>

  <main class="content">
    <h2 class="intro-title">Überschrift</h2>
    <p class="intro-text">Lorem ipsum dolor sit amet, arcu maiores quis nullam non, bibendum elit in nulla dolor laoreet, platea congue ut ultricies orci sollicitudin vestibu lum. Quam viverra lectus sit lectus suscipit sed, morbi eget aliquam lorem lorem, ornare sit, parturient at vestibulum orci quis mauris, facilisi dignissim nullam diam. Purus facilisi ducimus neque proin. Quam ligula aptent id vulputate, imperdiet ligula fusce mauris eget, laoreet est elit molestie maecenas cursus enim. Feugiat duis quis senectus, magna aliquam pede, quam in purus sit sed id. Tempus sed metus posuere aenean sollicitudin, aenean pede placerat, iaculis soluta, ipsum pede nulla sit dui. A turpis ac ut velit, leo et conubia egestas, fusce quis non, dolor magna penatibus quis et eget. Quis nec, sed sit arcu, quis lectus euismod at tempor, erat inceptos tristique. Fringilla dictumst ut libero quis augue. Rhoncus sed id dolore in sed et, vitae amet aenean, augue lacinia mus et, eros lacus elit eu pellentesque viverra. Ornare eu a ut id malesuada wisi.</p>

    <h2 class="col-left-title">Überschrift</h2>
    <p class="col-left-text">Lorem ipsum dolor sit amet, arcu maiores quis nullam non, bibendum elit in nulla dolor laoreet, platea congue ut ultricies orci sol&shy;licitudin vestibu lum. Quam viverra lectus sit lectus suscipit sed, morbi eget aliquam lorem lorem, ornare sit, parturient at vesti&shy;bulum orci quis mauris, facilisi dignissim nullam diam. Purus facilisi ducimus neque proin. Quam ligula aptent id vulputate, imperdiet ligula fusce mauris eget, viverra.</p>

    <h2 class="col-right-title">Überschrift</h2>
    <p class="col-right-text">Lorem ipsum dolor sit amet, arcu maiores quis nullam non, bibendum elit in nulla dolor laoreet, platea congue ut ultricies orci sol&shy;licitudin vestibu lum. Quam viverra lectus sit lectus suscipit sed, morbi eget aliquam lorem lorem, ornare sit, parturient at vesti&shy;bulum orci quis mauris, facilisi dignissim nullam diam. Purus facilisi ducimus neque proin. Quam ligula aptent id vulputate, imperdiet ligula fusce mauris eget, viverra.</p>
  </main>

  <footer class="site-footer">
    <a href="#">Startseite</a>
    <a href="#">Teilnahmebedingungen</a>
    <a href="#">Preisdetails</a>
    <a href="#">Teilnehmen</a>
    <a href="#">Datenschutz</a>
    <a href="#">Impressum</a>
  </footer>
</body>
</html>
```